Nutrition Company seeks label design for new product line CHIA Seeds TEA

Vembra Nutrition focuses on bringing natural nutritional/dietary supplements to the world.
We need a label design for a new product we are creating by combining instant tea granulate with organic chia seeds.  We have three flavors for introduction and will be adding more as the formulas are created.  The first three will be Ginger Tea, Harbor Tea, Cleansing Tea.
Exact nutritional facts are still being worked on and will be updated as it becomes available.  Ginger Tea nutritional facts is available.
Attached are files of label specification, samples that we like for you to use as inspirational ideas, a label of one of our product, logo (you are free to change the logo text style), and a product that uses the same container the label will be placed on.

Updates
White Wide Mouth Jar png file has been added for designers who wants to use it.  Product specification for ginger has been updated fixing minor grammatical errors.

Reason: Due to the holiday weekend, deadline has been extended so designers can enjoy the holiday.  Payment will be set to guaranteed.  Thank you for all who have submitted their designs.  Those who haven't submitted yet, please do!  We are eager to see your creativity and may use designs for future product lines.

If you are using a stock image please let us know.  We will look into the cost of paying for the stock image license rights to be used.  Thank you.

Target Market(s)
Health conscious individuals. Ages 25 - 60.
Industry/Entity Type
It Company
Requirements
Must have
- Final design must be print ready AI file with bleed.  And white plates if needed.

Nice to have
- "Chia Tea" in a fixed location with flavor, like Plomi Twist example in Chia Tea Sample document.
Refer to Chia Tea Samples document.

```html
<!DOCTYPE html>
<html lang="en">
<head>
<meta charset="utf-8">
<title>Vembra Nutrition – Chia Tea Labels</title>
<link href="https://fonts.googleapis.com/css2?family=Amatic+SC:wght@400;700&display=swap" rel="stylesheet">
<style>
  :root {
    --ink: #2b2b2b;
    --paper: #ffffff;
    --frame: #3a3a3a;
    --red: #e3210f;
    --green: #1f7a2a;
    --teal: #1ea3b3;
  }
  * { margin: 0; padding: 0; box-sizing: border-box; }
  html, body { width: 1200px; height: 713px; overflow: hidden; background: var(--paper); }
  body { position: relative; font-family: "Amatic SC", "Arial Narrow", sans-serif; color: var(--ink); }

  .brand-block { position: absolute; top: 44px; right: 92px; text-align: right; }
  .brand-name { display: flex; align-items: center; justify-content: flex-end; gap: 10px;
    font-weight: 700; font-size: 34px; line-height: 1; color: var(--ink); }
  .brand-dot { width: 34px; height: 34px; border: 4px solid var(--ink); border-radius: 50%; }
  .project-title { font-size: 46px; font-weight: 400; margin-top: 14px; letter-spacing: 1px; }

  .label { position: absolute; background: var(--paper); text-align: center; --accent: var(--red); }
  .label--main { left: 22px; top: 22px; width: 648px; height: 267px; border: 1px solid var(--frame); }
  .label--green { --accent: var(--green); }
  .label--teal { --accent: var(--teal); }

  .label__tagline { font-weight: 700; font-size: 13px; padding-top: 6px; }
  .label__maker { display: flex; align-items: center; justify-content: center; gap: 8px;
    margin-top: 16px; color: var(--accent); font-weight: 700; font-size: 20px; line-height: 1; }
  .label__ring { width: 40px; height: 40px; border: 4px solid var(--accent); border-radius: 50%; }
  .label__line { font-weight: 700; font-size: 58px; line-height: 0.9; margin-top: 12px; }
  .label__flavor { font-weight: 700; font-size: 40px; line-height: 0.9; color: var(--accent); }
  .label__claim { font-weight: 700; font-size: 15px; margin-top: 2px; }
  .label__band { position: absolute; left: 0; right: 0; bottom: 24px; height: 8px; background: var(--accent); }
  .label__weight { position: absolute; left: 0; right: 0; bottom: 3px; font-weight: 700; font-size: 15px; }

  .label--small { top: 400px; width: 340px; height: 230px; border: 1px solid #d4d4d4; }
  .label--small .label__tagline { font-size: 10px; padding-top: 8px; }
  .label--small .label__maker { font-size: 15px; margin-top: 14px; }
  .label--small .label__ring { width: 28px; height: 28px; border-width: 3px; }
  .label--small .label__line { font-size: 40px; margin-top: 12px; }
  .label--small .label__flavor { font-size: 28px; }
  .label--small .label__claim { font-size: 11px; }
  .label--small .label__band { height: 4px; bottom: 30px; }
  .label--small .label__weight { font-size: 11px; bottom: 8px; }
  .pos-left { left: 30px; }
  .pos-center { left: 430px; }
  .pos-right { left: 830px; }
</style>
</head>
<body>
  <header class="brand-block">
    <div class="brand-name"><span class="brand-dot"></span>Vembra Nutrition</div>
    <div class="project-title">Packaging Project</div>
  </header>

  <section class="label label--main">
    <p class="label__tagline">Instant tea granulate with organic chia seeds</p>
    <div class="label__maker"><span class="label__ring"></span>Vembra Nutrition</div>
    <h1 class="label__line">Chia Tea</h1>
    <h2 class="label__flavor">Harbor Tea</h2>
    <p class="label__claim">100% natural dietary supplements</p>
    <div class="label__band"></div>
    <p class="label__weight">Net wt. 250g</p>
  </section>

  <section class="label label--small label--green pos-left">
    <p class="label__tagline">Instant tea granulate with organic chia seeds</p>
    <div class="label__maker"><span class="label__ring"></span>Vembra Nutrition</div>
    <h2 class="label__line">Chia Tea</h2>
    <h3 class="label__flavor">Ginger Tea</h3>
    <p class="label__claim">100% natural dietary supplements</p>
    <div class="label__band"></div>
    <p class="label__weight">Net wt. 250g</p>
  </section>

  <section class="label label--small pos-center">
    <p class="label__tagline">Instant tea granulate with organic chia seeds</p>
    <div class="label__maker"><span class="label__ring"></span>Vembra Nutrition</div>
    <h2 class="label__line">Chia Tea</h2>
    <h3 class="label__flavor">Harbor Tea</h3>
    <p class="label__claim">100% natural dietary supplements</p>
    <div class="label__band"></div>
    <p class="label__weight">Net wt. 250g</p>
  </section>

  <section class="label label--small label--teal pos-right">
    <p class="label__tagline">Instant tea granulate with organic chia seeds</p>
    <div class="label__maker"><span class="label__ring"></span>Vembra Nutrition</div>
    <h2 class="label__line">Chia Tea</h2>
    <h3 class="label__flavor">Cleansing Tea</h3>
    <p class="label__claim">100% natural dietary supplements</p>
    <div class="label__band"></div>
    <p class="label__weight">Net wt. 250g</p>
  </section>
</body>
</html>
```